Packaging Design Project for a Pet Product Company

Need a packaging design for a pet product company based in Los Angeles. We offer user-friendly pet products to people. This new product is a Collapsible Pet Bowl that folds in 4 ways for dogs of all sizes. It can be used for food or water. It is light-weight, functional and eco-friendly. Great for indoor/outdoor use at home and it's easy to take on the go.

www.tumblecove.com - get the look and feel of our design.
(This project is for a new bowl which is not yet announced on our website.)

I can be reached via the MockupHarbor comment board or at rona581@quillmail.net.

Target Market(s)

Pet boutique owners and customers

Industry/Entity Type

It Company

Requirements
Must have
• Use kraft paper as the background color of the design

Maintain a Modern, fun, creative and eco-friendly look in the design

color scheme:
Background color: kraft paper
Design & Font color: WHITE and CHARCOAL GREY are must. Possibly a 3rd color (Tumble Cove logo green or any 3rd color of your choice)

Maintain consistency with our "existing packaging for current product line" (see attached file)

Picture of a Labradoodle dog with a bowl in front of the dog (black and white)
Nice to have
• Play around with the composition/layout of the design and suggest any creative touch to make it better

Modify the wording/content if necessary

Mock-up rendering should be as realistic as possible

Use one of our bowl color in mock-up rendering. Same packaging for pink bowl and the green bowl.

```html
<!DOCTYPE html>
<html lang="en">
<head>
<meta charset="utf-8">
<title>Tumble Cove Collapsible Pet Bowl Packaging</title>
<link rel="stylesheet" href="https://fonts.googleapis.com/css2?family=Comic+Neue:wght@400;700&display=swap">
<style>
  :root {
    --stage: #ebe6dd;
    --kraft: #e4cfa4;
    --kraft-deep: #d3ba89;
    --kraft-band: #c9ad79;
    --charcoal: #47423c;
    --ink: #5a4a38;
    --white: #ffffff;
    --photo-dark: #5b5650;
    --photo-light: #a19a91;
  }
  * { box-sizing: border-box; margin: 0; padding: 0; }
  html, body { width: 1200px; height: 812px; overflow: hidden; }
  body {
    position: relative;
    background: var(--stage);
    font-family: "Comic Neue", "Comic Sans MS", cursive;
    color: var(--charcoal);
  }
  .card { position: absolute; }

  /* front panel */
  .front-header {
    position: absolute; left: 160px; top: 0; width: 280px; height: 200px;
    background: var(--kraft);
  }
  .hang-hole {
    position: absolute; left: 50%; top: 14px; width: 44px; height: 10px;
    margin-left: -22px; border: 1.5px solid #c98a8a; border-radius: 6px;
  }
  .brand {
    position: absolute; left: 0; right: 0; display: flex;
    align-items: center; justify-content: center; gap: 10px;
    font-weight: 700; color: var(--charcoal); letter-spacing: 0.5px;
  }
  .brand-mark { width: 30px; height: 30px; border-radius: 50%; background: var(--charcoal); }
  .front-header .brand { top: 96px; font-size: 30px; }
  .url {
    position: absolute; left: 0; right: 0; text-align: center;
    font-size: 15px; font-weight: 700; color: var(--ink); letter-spacing: 1px;
  }
  .front-header .url { top: 164px; }
  .front-header .rule {
    position: absolute; left: 0; right: 0; top: 152px; height: 2px; background: var(--kraft-band);
  }
  .front-body {
    position: absolute; left: 96px; top: 196px; width: 381px; height: 616px;
    background: var(--kraft); border-radius: 190px 190px 0 0;
    text-align: center;
  }
  .front-title-small { position: absolute; top: 30px; left: 0; right: 0; font-size: 32px; font-weight: 700; }
  .front-title-large { position: absolute; top: 72px; left: 0; right: 0; font-size: 50px; font-weight: 700; }
  .hero-photo {
    position: absolute; left: 120px; top: 146px; width: 170px; height: 310px;
    border-radius: 70px 70px 40px 40px;
    background: linear-gradient(180deg, var(--photo-dark) 0%, var(--photo-dark) 65%, var(--photo-light) 100%);
  }
  .paw-spot { position: absolute; width: 34px; height: 34px; border-radius: 50%; background: var(--kraft-deep); }
  .size-row {
    position: absolute; top: 478px; left: 120px; width: 150px; height: 22px;
    border-radius: 8px; background: linear-gradient(90deg, var(--photo-dark), var(--photo-light));
  }
  .front-copy {
    position: absolute; top: 518px; left: 0; right: 0;
    font-size: 17px; font-weight: 700; line-height: 22px; color: var(--charcoal);
  }

  /* back panel */
  .back {
    position: absolute; left: 785px; top: 0; width: 335px; height: 812px;
    background: var(--kraft);
  }
  .back .hang-hole { top: 16px; }
  .back .brand { top: 122px; font-size: 30px; }
  .back .url { top: 205px; }
  .title-band {
    position: absolute; left: 0; right: 0; top: 250px; height: 78px;
    background: var(--kraft-deep); display: flex; align-items: center; justify-content: center;
    font-size: 26px; font-weight: 700;
  }
  .fold-note {
    position: absolute; left: 22px; top: 344px; width: 60px;
    font-size: 11px; line-height: 13px; color: var(--ink);
  }
  .fold-arrow { position: absolute; left: 6px; top: 344px; }
  .fold-diagram {
    position: absolute; left: 96px; top: 340px; width: 210px; height: 80px;
    border-radius: 12px; background: linear-gradient(90deg, var(--photo-light), var(--photo-dark));
  }
  .feature-box {
    position: absolute; left: 22px; right: 30px;
    background: var(--kraft-band); padding: 8px 12px;
    font-size: 14px; font-weight: 700; line-height: 20px; color: var(--charcoal);
    text-align: center;
  }
  .feature-box.primary { top: 440px; height: 78px; padding-top: 9px; }
  .feature-box.secondary { top: 530px; height: 170px; }
  .feature-box li { list-style: none; }
  .feature-box li::before { content: "\2022 "; }
  .spec-list {
    position: absolute; left: 22px; top: 714px; width: 170px;
    font-size: 11px; line-height: 13px; color: var(--ink);
  }
  .upc-box {
    position: absolute; left: 212px; top: 714px; width: 64px; height: 60px;
    background: var(--white); display: flex; align-items: center; justify-content: center;
    font-family: Arial, sans-serif; font-size: 18px; color: #222;
  }
</style>
</head>
<body>
  <section class="card front" aria-label="Front panel">
    <div class="front-header">
      <span class="hang-hole"></span>
      <div class="brand"><span class="brand-mark"></span>Tumble Cove</div>
      <div class="rule"></div>
      <div class="url">www.tumblecove.com</div>
    </div>
    <div class="front-body">
      <h1 class="front-title-small">Collapsible</h1>
      <h2 class="front-title-large">Pet Bowl</h2>
      <div class="hero-photo" role="img" aria-label="Black and white photo of a puppy sitting behind a collapsible silicone bowl"></div>
      <span class="paw-spot" role="img" aria-label="Paw print" style="left:44px; top:200px"></span>
      <span class="paw-spot" role="img" aria-label="Paw print" style="left:22px; top:300px"></span>
      <span class="paw-spot" role="img" aria-label="Paw print" style="left:56px; top:390px"></span>
      <span class="paw-spot" role="img" aria-label="Paw print" style="left:300px; top:200px"></span>
      <span class="paw-spot" role="img" aria-label="Paw print" style="left:326px; top:276px"></span>
      <span class="paw-spot" role="img" aria-label="Paw print" style="left:304px; top:380px"></span>
      <div class="size-row" role="img" aria-label="Bowl shown at four collapsed sizes"></div>
      <p class="front-copy">100% Silicone<br>Adjustable to 4 different sizes<br>it's like having 4 bowls in one!</p>
    </div>
  </section>

  <section class="back" aria-label="Back panel">
    <span class="hang-hole"></span>
    <div class="brand"><span class="brand-mark"></span>Tumble Cove</div>
    <div class="url">www.tumblecove.com</div>
    <div class="title-band">Collapsible Pet Bowl</div>
    <svg class="fold-arrow" width="12" height="48" viewBox="0 0 12 48" aria-hidden="true">
      <path d="M6 2 V46 M2 7 L6 2 L10 7 M2 41 L6 46 L10 41" stroke="#5a4a38" stroke-width="1.5" fill="none"/>
    </svg>
    <p class="fold-note">Fold down to only 1.5 inches</p>
    <div class="fold-diagram" role="img" aria-label="Drawing of the bowl folded flat and expanded"></div>
    <ul class="feature-box primary">
      <li>Adjustable to 4 different sizes</li>
      <li>Easy to clean</li>
      <li>Non-slip design</li>
    </ul>
    <ul class="feature-box secondary">
      <li>Lightweight, Functional and Eco-friendly</li>
      <li>For dogs of all sizes</li>
      <li>No splattered mess</li>
      <li>Use for food or water</li>
      <li>Great for indoor/outdoor use at home and easy to take on the go</li>
    </ul>
    <p class="spec-list">64 oz. / 8 cups Capacity<br>Fold down to only 1.5 inches<br>100% Food Grade Silicone<br>Dishwasher Safe (Top Rack)<br>FDA Food-Safe Silicone</p>
    <div class="upc-box">UPC</div>
  </section>
</body>
</html>
```